R.T. Framers Postcard Design

We need a postcard designed around the utility rebates for window installations. For customers who have Electric heated homes can receive $6 per square foot for each window and patio door and for Natural gas heated homes, they can get $75.00 per window and patio door. The $6 per square foot for electric heated customers is the better rebate averaging about $1000.00 for a house with 10 windows and a patio door. Our Company colors are maroon, black and white, we would like to have a post card designed around these colors. The postcard should be designed to share about these 2 rebates and having a window installation theme. You can use pictures off of our website...www.rtframers-example.com

Target Market(s)

Homeowners with electric heat or Natural gas heat

Industry/Entity Type

Utility

Requirements
Must have
• Blank white square on the back for me to hand write address information.

```html
<!DOCTYPE html>
<html lang="en">
<head>
<meta charset="utf-8">
<title>R.T. Framers Postcard</title>
<link rel="stylesheet" href="https://fonts.googleapis.com/css2?family=Open+Sans:wght@400;600;700&family=Roboto:ital,wght@0,300;0,400;0,700;0,900;1,300&display=swap">
<style>
  :root {
    --maroon: #8a1c20;
    --maroon-deep: #5e0e12;
    --black: #111111;
    --white: #ffffff;
    --grey-panel: #cfcfcf;
    --grey-text: #333333;
    --orange: #e38a2b;
    --stage: #232323;
  }
  * { box-sizing: border-box; margin: 0; padding: 0; }
  html, body { width: 1200px; height: 1200px; overflow: hidden; }
  body { background: var(--stage); position: relative; font-family: "Open Sans", sans-serif; }

  /* ---------- back side ---------- */
  .card-back {
    position: absolute; left: 419px; top: 26px; width: 727px; height: 560px;
    background: var(--white);
  }
  .offer-panel { position: absolute; left: 0; top: 0; width: 352px; height: 468px; }
  .offer-photo {
    height: 160px;
    background: linear-gradient(135deg, #c9b878 0%, #8fae6a 45%, #e8e6d8 70%, #3c3f33 100%);
    border-bottom: 3px solid var(--black);
  }
  .offer-rates {
    height: 208px; background: var(--grey-panel);
    text-align: center; padding-top: 8px; color: var(--grey-text);
  }
  .rate-title { font-family: "Roboto", sans-serif; font-weight: 900; font-size: 22px; color: var(--maroon); line-height: 26px; }
  .rate-value { font-family: "Roboto", sans-serif; font-weight: 700; font-size: 20px; color: var(--grey-text); line-height: 24px; margin-bottom: 8px; }
  .rate-note { font-size: 13px; line-height: 19px; padding: 0 20px; }
  .offer-contact {
    height: 100px; background: var(--black); color: var(--white); text-align: center;
    padding-top: 8px;
  }
  .contact-heading { font-family: "Roboto", sans-serif; font-weight: 900; font-size: 22px; line-height: 28px; }
  .contact-line { display: flex; justify-content: center; align-items: center; gap: 8px; font-size: 18px; line-height: 30px; }
  .contact-line svg { flex: none; }
  .contact-gap { width: 12px; }

  .sender { position: absolute; left: 364px; top: 12px; }
  .sender-name { display: flex; align-items: center; gap: 8px; font-family: "Roboto", sans-serif; font-weight: 700; font-size: 20px; color: var(--maroon); height: 66px; }
  .sender-square { width: 18px; height: 18px; background: var(--maroon); }
  .sender-address { font-size: 16px; line-height: 22px; color: var(--grey-text); margin-top: 2px; }
  .address-box {
    position: absolute; left: 551px; top: 12px; width: 166px; height: 166px;
    border: 1px solid #9a9a9a; background: var(--white);
  }

  /* ---------- front side ---------- */
  .card-front {
    position: absolute; left: 64px; top: 612px; width: 729px; height: 562px;
    background: linear-gradient(160deg, var(--maroon) 0%, #7a1418 55%, var(--maroon-deep) 100%);
    overflow: hidden;
  }
  .guide { position: absolute; background: rgba(255,255,255,0.3); z-index: 0; }
  .guide-h { left: 0; width: 100%; height: 1px; }
  .guide-v { top: 0; height: 100%; width: 1px; }
  .front-header {
    position: absolute; left: 0; top: 18px; width: 100%; height: 52px; z-index: 2;
    background: var(--black); color: var(--white);
    font-family: "Roboto", sans-serif; font-weight: 300; font-size: 38px;
    line-height: 52px; padding-left: 28px; letter-spacing: 0.3px;
  }
  .front-photo { position: absolute; z-index: 1; border: 1px solid rgba(255,255,255,0.6); }
  .photo-corner { left: 28px; top: 86px; width: 221px; height: 139px; background: linear-gradient(135deg, #eef0ea 0%, #9cbf84 50%, #b54a3e 100%); }
  .photo-living { left: 28px; top: 240px; width: 221px; height: 138px; background: linear-gradient(160deg, #c8a46a 0%, #9bb37a 45%, #6e4e33 100%); }
  .photo-feature { left: 266px; top: 86px; width: 433px; height: 292px; background: linear-gradient(110deg, #e9ecdf 0%, #c6d4b4 45%, #f3f1ea 75%, #d9c7a4 100%); }
  .front-brand {
    position: absolute; left: 18px; top: 391px; width: 239px; height: 152px; z-index: 1;
    background: var(--white); display: flex; align-items: center; justify-content: center; gap: 10px;
    font-family: "Roboto", sans-serif; font-weight: 700; font-size: 30px; color: var(--maroon);
  }
  .brand-square { width: 24px; height: 24px; background: var(--maroon); flex: none; }
  .front-tagline {
    position: absolute; right: 34px; top: 420px; text-align: right; color: var(--white); z-index: 1;
    font-family: "Roboto", sans-serif; font-style: italic; font-weight: 300; font-size: 28px; line-height: 33px;
  }
  .front-url {
    position: absolute; right: 34px; top: 492px; color: var(--orange); z-index: 1;
    font-family: "Roboto", sans-serif; font-weight: 700; font-size: 25px;
  }
</style>
</head>
<body>

<section class="card-back" aria-label="Postcard back">
  <div class="offer-panel">
    <div class="offer-photo" role="img" aria-label="Living room with large white-framed windows overlooking a garden and a leather sofa"></div>
    <div class="offer-rates">
      <p class="rate-title">Electric Heated Homes</p>
      <p class="rate-value">$6 per square foot</p>
      <p class="rate-title">Natural Gas Heated Homes</p>
      <p class="rate-value">$75.00 per window and patio door</p>
      <p class="rate-note">Averaging about $1000.00<br>for a house with 10 windows and a patio door<br>for only $6 per square foot Electric Heated Customers.</p>
    </div>
    <div class="offer-contact">
      <p class="contact-heading">Contact Us Today!</p>
      <p class="contact-line">
        <svg width="16" height="16" viewBox="0 0 16 16" aria-hidden="true"><path d="M3 1.5l3 3-1.6 1.8c.8 1.8 2.2 3.2 4 4L10.2 8.7l3 3-2 2C6 13.4 2.6 10 1.3 3.5z" fill="#b8262b"/></svg>
        <span>360-555-0147</span><span class="contact-gap"></span>
        <svg width="12" height="18" viewBox="0 0 12 18" aria-hidden="true"><rect x="1" y="1" width="10" height="16" rx="2" fill="#b8262b"/><rect x="3" y="3" width="6" height="9" fill="#111"/></svg>
        <span>425-555-0182</span>
      </p>
      <p class="contact-line">
        <svg width="16" height="12" viewBox="0 0 16 12" aria-hidden="true"><rect x="0.5" y="0.5" width="15" height="11" rx="2" fill="#b8262b"/><path d="M1 1.5l7 5 7-5" stroke="#111" stroke-width="1.2" fill="none"/></svg>
        <span>admin@rtframers-example.com</span>
      </p>
    </div>
  </div>

  <div class="sender">
    <p class="sender-name"><span class="sender-square"></span>R.T. Framers</p>
    <p class="sender-address">1250 Cedar Lane NE<br>Brookfield, Washington<br>98000, United States</p>
  </div>
  <div class="address-box" aria-label="Blank space for handwritten address"></div>
</section>

<section class="card-front" aria-label="Postcard front">
  <span class="guide guide-h" style="top:232px"></span>
  <span class="guide guide-h" style="top:385px"></span>
  <span class="guide guide-v" style="left:18px"></span>
  <span class="guide guide-v" style="left:257px"></span>
  <span class="guide guide-v" style="left:710px"></span>
  <h1 class="front-header">Custom Windows &amp; Door Installation</h1>
  <div class="front-photo photo-corner" role="img" aria-label="Sunlit corner room with white double-hung windows and a wicker chair"></div>
  <div class="front-photo photo-living" role="img" aria-label="Living room with a wide picture window looking onto autumn trees"></div>
  <div class="front-photo photo-feature" role="img" aria-label="Woman with a cup standing beside tall white vinyl windows"></div>
  <div class="front-brand"><span class="brand-square"></span>R.T. Framers</div>
  <p class="front-tagline">Installing windows the right way<br>every time since 1985</p>
  <p class="front-url">www.rtframers-example.com</p>
</section>

</body>
</html>
```